Buch-/eBook-Cover für Frauen zwischen 16-35
Zielgruppe
MLT/ Mellow Lantern Typesetting. Ich suche Unterstützung für die Erstellung eines Buchcovers für Frauen zwischen 16-35.
Aufgabenstellung
Ich habe eine Zusammenfassung des Projektes in dem beigefügten Word Dokument zusammen mit Beispielcovern, Covern der Konkurrenz etc.

```html
<!DOCTYPE html>
<html lang="de">
<head>
<meta charset="UTF-8">
<title>Das große Mutproben-Buch für Seelenfreundinnen – Cover</title>
<link href="https://fonts.googleapis.com/css2?family=Oswald:wght@500;600&family=Dancing+Script:wght@700&family=Patrick+Hand&family=Nunito:wght@400;600&display=swap" rel="stylesheet">
<style>
  :root {
    --canvas-bg: #f6e6e1;
    --front-bg-top: #f4efe8;
    --front-bg-bottom: #efe4d8;
    --title-ink: #55605b;
    --script-ink: #2b2a2a;
    --art-peach: #eab79c;
    --art-sage: #7f9a89;
    --art-sun: #e9a25a;
    --art-blush: #f2d3c3;
    --label-bg: #ffffff;
    --label-ink: #3a3636;
    --back-bg: #efd9cf;
    --back-panel: #f7e6de;
    --back-text: #e07a68;
    --back-heading: #3b3838;
    --back-accent: #f2a23c;
  }
  * { box-sizing: border-box; margin: 0; padding: 0; }
  html, body { width: 1200px; height: 1200px; overflow: hidden; }
  body {
    background: var(--canvas-bg);
    position: relative;
    font-family: "Nunito", sans-serif;
  }

  /* Front cover */
  .front-cover {
    position: absolute;
    left: 90px; top: 250px;
    width: 500px; height: 700px;
    background: linear-gradient(180deg, var(--front-bg-top), var(--front-bg-bottom));
    overflow: hidden;
    box-shadow: 0 10px 30px rgba(120, 80, 70, 0.15);
  }
  .front-title {
    position: absolute;
    top: 50px; left: 0; right: 0;
    text-align: center;
    font-family: "Oswald", sans-serif;
    font-weight: 600;
    font-size: 42px;
    line-height: 1.15;
    letter-spacing: 1px;
    color: var(--title-ink);
    text-transform: uppercase;
  }
  .front-script {
    position: absolute;
    top: 156px; left: 0; right: 0;
    text-align: center;
    font-family: "Dancing Script", cursive;
    font-weight: 700;
    font-size: 42px;
    color: var(--script-ink);
  }
  .front-art {
    position: absolute;
    left: 0; right: 0; bottom: 0;
    height: 470px;
    background:
      radial-gradient(circle at 30% 40%, var(--art-sun) 0 70px, transparent 71px),
      radial-gradient(ellipse at 50% 60%, var(--art-sage) 0 110px, transparent 180px),
      radial-gradient(ellipse at 80% 85%, var(--art-peach) 0 120px, transparent 200px),
      linear-gradient(180deg, transparent, var(--art-blush));
  }
  .front-subtitle {
    position: absolute;
    left: 70px; bottom: 60px;
    width: 330px;
    padding: 12px 18px;
    background: var(--label-bg);
    border-radius: 10px;
    font-family: "Patrick Hand", cursive;
    font-size: 26px;
    line-height: 1.2;
    color: var(--label-ink);
    text-align: center;
  }

  /* Back cover */
  .back-cover {
    position: absolute;
    left: 650px; top: 280px;
    width: 460px; height: 640px;
    background: var(--back-bg);
    overflow: hidden;
    box-shadow: 0 10px 30px rgba(120, 80, 70, 0.12);
  }
  .back-accent {
    position: absolute;
    top: -40px; right: -40px;
  }
  .back-heading {
    margin-top: 48px;
    text-align: center;
    font-family: "Oswald", sans-serif;
    font-weight: 600;
    font-size: 24px;
    letter-spacing: 0.5px;
    color: var(--back-heading);
  }
  .back-tagline {
    margin-top: 4px;
    text-align: center;
    font-family: "Dancing Script", cursive;
    font-weight: 700;
    font-size: 26px;
    line-height: 1.15;
    color: var(--back-heading);
  }
  .back-panel {
    position: absolute;
    left: 30px; right: 30px; top: 172px;
    height: 400px;
    padding: 22px 24px;
    background: var(--back-panel);
    border-radius: 16px;
  }
  .back-panel p {
    font-size: 14.5px;
    line-height: 1.5;
    color: var(--back-text);
    text-align: center;
    margin-bottom: 16px;
  }
  .back-panel p:last-child { margin-bottom: 0; }
  .back-ornament {
    position: absolute;
    left: 16px; bottom: 12px;
    width: 48px; height: 48px;
    border-radius: 50%;
    background: radial-gradient(circle, #e8937f, transparent 70%);
  }
</style>
</head>
<body>
  <section class="front-cover">
    <h1 class="front-title">Das große<br>Mutproben-Buch</h1>
    <p class="front-script">für Seelenfreundinnen</p>
    <div class="front-art" role="img" aria-label="Illustration zweier Freundinnen von hinten mit Sonne und Pflanzen"></div>
    <p class="front-subtitle">Zusammen wachsen, lachen und die Welt entdecken</p>
  </section>

  <section class="back-cover">
    <svg class="back-accent" width="110" height="110" viewBox="0 0 110 110" aria-hidden="true">
      <circle cx="55" cy="55" r="55" fill="var(--back-accent)"/>
    </svg>
    <h2 class="back-heading">VON ALLTAG ZU ABENTEUER:</h2>
    <p class="back-tagline">Entdeckt die Magie<br>gemeinsamer Erlebnisse</p>
    <div class="back-panel">
      <p>Das Mutproben-Buch für Seelenfreundinnen bietet euch 52 abwechslungsreiche Aktivitäten, die euch ein Jahr voller Spaß, Abenteuer und unvergesslicher Erinnerungen bescheren. Ein Jahr, das eure Freundschaft für immer stärken wird.</p>
      <p>Von spannenden Outdoor-Abenteuern bis hin zu kreativen DIY-Projekten – jede Woche bringt die perfekte Aktivität und die nötige Abwechslung in euren Alltag. Stärkt eure Freundschaft, lacht gemeinsam und genießt die kostbare Zeit miteinander.</p>
      <p>Entdeckt, wie viel Freude und Abwechslung das Leben bietet, wenn ihr es zusammen erlebt. Macht jede Woche zu etwas Besonderem – mit dem Mutproben-Buch für Seelenfreundinnen!</p>
    </div>
    <div class="back-ornament" role="img" aria-label="Kleines florales Zweig-Ornament"></div>
  </section>
</body>
</html>
```